Cedarbrook Ridge Footraces

We need a website (wordpress) design for a new website that we will be launching. This is for a new trail racing series in Canada.
We recently had a logo designed so want to incorporate the colours of the logo on the website design. Especially the dark blue, green and orange.
Websites that we like for comparison of trail running race themes are:
https://www.mossyloopevents.com/
https://www.bramblerunfest.com/
http://www.quillpathcircuit.ca/
https://www.ferncrestroutes.com/
http://www.thornwickdashgroup.com/

Target Market(s)

Outdoor trail runners

Coding

Coded - Design and coding required

Number of Pages Required

4 page

Font styles to use
Sans Serif

Colors
0255a3
33b8a4
f37122

Requirements
Must have
• There will be a main page with eye catching design noting what we do. Page 2 and 3 will be for each race in the series. Page 1 will be a specific race, and page 2 with be for another race. page 3 and 4 will be for future races that we add so that each race has their own page.
• Our races all take place in the mountains, so using graphics including mountains, rivers, trees is all a requirement for us.
• Our logo is attached, we want to use the colours of the logo in the website design.
Nice to have
• Outdoor theme is a nice to have. We like wood and earth tone colours, and pictures/graphics of runners and mountains and trees.
• There are 4 people involved in our organization. We'd like a photo and brief blurb of each of us, similar to how this website did their layout: https://www.mossyloopevents.com/

```html
<!DOCTYPE html>
<html lang="en">
<head>
<meta charset="utf-8">
<title>Cedarbrook Ridge Footraces</title>
<link href="https://fonts.googleapis.com/css2?family=Arimo:wght@400;700&display=swap" rel="stylesheet">
<style>
  :root {
    --brand-blue: #0255a3;
    --brand-teal: #33b8a4;
    --brand-orange: #f37122;
    --nav-orange: #f07a1e;
    --text-dark: #111;
    --white: #fff;
  }
  * { margin: 0; padding: 0; box-sizing: border-box; }
  html, body { width: 1200px; height: 1200px; overflow: hidden; }
  body { font-family: "Arimo", Arial, sans-serif; position: relative; background: var(--brand-teal); }

  .hero { position: absolute; left: 0; top: 0; width: 1200px; height: 798px; }
  .hero-photo {
    position: absolute; inset: 0;
    background:
      radial-gradient(ellipse 320px 420px at 520px 360px, #5a5446 0%, rgba(60,58,46,0.6) 45%, transparent 80%),
      linear-gradient(160deg, #1f2a1d 0%, #26301f 40%, #141c14 75%, #0d120d 100%);
  }
  .brand {
    position: absolute; left: 48px; top: 52px;
    display: flex; align-items: center; gap: 8px;
    font-size: 18px; font-weight: 700; color: var(--brand-blue);
  }
  .brand-dot { width: 16px; height: 16px; border-radius: 50%; background: var(--brand-blue); }

  .main-nav { position: absolute; top: 55px; left: 0; }
  .main-nav a {
    position: absolute; white-space: nowrap;
    font-size: 24px; color: var(--nav-orange); text-decoration: none;
  }

  .hero-title {
    position: absolute; top: 310px; left: 0; width: 1200px; text-align: center;
    font-size: 50px; font-weight: 700; color: var(--brand-blue); letter-spacing: 0.5px;
  }
  .hero-sub {
    position: absolute; top: 380px; left: 0; width: 1200px; text-align: center;
    font-size: 28px; color: var(--white);
  }
  .join-btn {
    position: absolute; left: 544px; top: 442px; width: 112px; height: 43px;
    background: var(--brand-orange); color: var(--white);
    font-size: 17px; display: flex; align-items: center; justify-content: center;
  }
  .slider-arrow { position: absolute; top: 400px; width: 62px; height: 62px; }
  .slider-arrow.prev { left: 27px; }
  .slider-arrow.next { left: 1108px; }

  .races {
    position: absolute; left: 0; top: 798px; width: 1200px; height: 402px;
    background: var(--brand-teal); border-top: 2px solid #8a8f8e;
  }
  .race-card { position: absolute; width: 230px; }
  .race-photo { width: 210px; height: 184px; }
  .race-title { position: absolute; font-size: 19px; color: var(--text-dark); white-space: nowrap; }
  .race-text { position: absolute; font-size: 14px; line-height: 16px; color: var(--text-dark); }
  .race-link { position: absolute; font-size: 13px; color: var(--brand-orange); text-decoration: none; }
</style>
</head>
<body>
  <header class="hero">
    <div class="hero-photo" role="img" aria-label="Photo of two hikers with trekking poles walking a leafy forest trail"></div>

    <div class="brand"><span class="brand-dot"></span>Cedarbrook Ridge</div>

    <nav class="main-nav">
      <a href="#" style="left:392px">Home</a>
      <a href="#" style="left:489px">About Us</a>
      <a href="#" style="left:621px">Races</a>
      <a href="#" style="left:715px">Our Team</a>
      <a href="#" style="left:857px">Contact Us</a>
    </nav>

    <h1 class="hero-title">CEDARBROOK RIDGE</h1>
    <p class="hero-sub">Footraces</p>
    <a class="join-btn">Join</a>

    <svg class="slider-arrow prev" viewBox="0 0 62 62" aria-label="Previous slide">
      <circle cx="31" cy="31" r="29" fill="none" stroke="#9a9a9a" stroke-width="2"/>
      <path d="M38 18 L16 31 L38 44 L31 31 Z" fill="#a8a8a8"/>
    </svg>
    <svg class="slider-arrow next" viewBox="0 0 62 62" aria-label="Next slide">
      <circle cx="31" cy="31" r="29" fill="none" stroke="#9a9a9a" stroke-width="2"/>
      <path d="M24 18 L46 31 L24 44 L31 31 Z" fill="#a8a8a8"/>
    </svg>
  </header>

  <section class="races">
    <article class="race-card" style="left:242px; top:71px">
      <div class="race-photo" role="img" aria-label="Photo of a smiling runner with a race bib in open grassland" style="background:linear-gradient(180deg,#8e9aa6 0%,#a7aeb2 50%,#7a6a4c 75%,#9b845c 100%)"></div>
    </article>
    <article class="race-card" style="left:490px; top:69px">
      <div class="race-photo" role="img" aria-label="Photo of a runner on a wooden bridge surrounded by green trees" style="background:linear-gradient(180deg,#3f6a2a 0%,#6f9a3e 45%,#557a33 70%,#8a8474 100%)"></div>
    </article>
    <article class="race-card" style="left:744px; top:71px">
      <div class="race-photo" role="img" aria-label="Photo of a runner on a forest dirt trail" style="background:linear-gradient(180deg,#7f8a6a 0%,#5f6b45 40%,#8a7460 70%,#5e9a3a 100%)"></div>
    </article>

    <h2 class="race-title" style="left:239px; top:276px; font-weight:400">Mountain Race</h2>
    <p class="race-text" style="left:242px; top:300px">Lorem ipsum dolor sit amet,<br>consectetur adipisicing elit</p>
    <a class="race-link" href="#" style="left:241px; top:337px">More details</a>

    <h2 class="race-title" style="left:490px; top:276px; font-weight:400">Valley Race</h2>
    <p class="race-text" style="left:488px; top:300px">Lorem ipsum dolor sit amet,<br>consectetur adipisicing elit</p>
    <a class="race-link" href="#" style="left:490px; top:337px">More details</a>

    <h2 class="race-title" style="left:744px; top:274px; font-weight:400">Future Race</h2>
    <p class="race-text" style="left:746px; top:300px">Lorem ipsum dolor sit amet,<br>consectetur adipisicing elit</p>
    <a class="race-link" href="#" style="left:746px; top:337px">More details</a>
  </section>
</body>
</html>
```